Business Card / Appointment Card for Physician

On one side it should give the logo, address, and contact information, and on the other side it should br an Appointment card.

One Side:
Logo (see attached files)
Board Certified American Orthopedic Surgery

1487 Harrowgate Ave.
Suite KM7
Bronx, NY 10527
Tel: (718) 552 - 1948
Fax: (718) 552 - 7210

628 Fourth Ave.
Suite 42
New York, NY 10087
Tel: (212) 734 - 2815

Second Side:
Appointment
give them a choice of Bronx or Mahattan office
For:
Date:
Time:

If you are unable to keep your appointment, please call (718) 263-5102 24hrs in advance.

Target Market(s)

People that need orthopedic surgery

Industry/Entity Type

Business

Contact Information for Business Card

smart and attractive

Requirements
Must have
• logo
• contact information on one side, appointment information on the other

```html
<!DOCTYPE html>
<html lang="en">
<head>
<meta charset="utf-8">
<title>Daniel R. Whitcombe MD PC – Business &amp; Appointment Card</title>
<link href="https://fonts.googleapis.com/css2?family=Roboto:wght@300;400;500;700&family=Roboto+Condensed:wght@400&display=swap" rel="stylesheet">
<style>
  :root {
    --bg: #d5d5d5;
    --card: #ffffff;
    --brand-blue: #3e6089;
    --brand-dark: #253a5a;
    --brand-green: #6ab04c;
    --text-gray: #555555;
    --rule: #6f8bb0;
  }
  * { box-sizing: border-box; margin: 0; padding: 0; }
  html, body { width: 1200px; height: 1200px; overflow: hidden; background: var(--bg); }
  body { position: relative; font-family: "Roboto", sans-serif; }

  .card {
    position: absolute;
    left: 192px;
    width: 813px;
    background: var(--card);
    box-shadow: 0 22px 26px -14px rgba(0,0,0,0.35);
  }
  .card--front { top: 86px; height: 455px; }
  .card--back { top: 596px; height: 450px; }

  /* Front: identity */
  .identity-mark {
    position: absolute; left: 361px; top: 40px;
    width: 90px; height: 90px; border-radius: 50%;
    background: var(--brand-blue);
  }
  .practice-name {
    position: absolute; left: 0; right: 0; top: 146px;
    text-align: center; font-size: 34px; font-weight: 400;
    color: var(--brand-blue); letter-spacing: -0.5px;
  }
  .practice-tagline {
    position: absolute; left: 0; right: 0; top: 186px;
    text-align: center; font-size: 18px; font-weight: 400;
    color: var(--brand-blue);
  }

  .credential-banner {
    position: absolute; left: 68px; top: 221px;
    width: 676px; height: 44px;
    background: var(--brand-green);
    border-radius: 4px 4px 0 0;
    color: #fff; font-size: 27px; font-weight: 500;
    text-align: center; line-height: 46px;
  }
  .fold { position: absolute; top: 248px; }

  .contact-band {
    position: absolute; left: 0; right: 0; top: 264px; height: 173px;
    background: var(--brand-blue);
  }
  .contact-band__base {
    position: absolute; left: 0; right: 0; top: 437px; height: 18px;
    background: var(--brand-dark);
  }
  .office {
    position: absolute;
    font-family: "Roboto Condensed", sans-serif;
    font-size: 27px; color: #fff;
  }
  .office__rule {
    position: absolute; left: -18px; top: 4px; width: 4px;
    background: #fff;
  }
  .office__pointer { position: absolute; }
  .office--bronx { left: 98px; top: 283px; line-height: 35px; }
  .office--bronx .office__rule { height: 130px; }
  .office--bronx .office__pointer { left: -32px; top: 55px; }
  .office--manhattan { left: 461px; top: 283px; line-height: 32px; }
  .office--manhattan .office__rule { left: -14px; height: 130px; }
  .office--manhattan .office__pointer { left: -28px; top: 55px; }

  /* Back: appointment */
  .appointment-tab {
    position: absolute; left: 214px; top: 0; width: 381px; height: 66px;
    background: var(--brand-blue);
    border-radius: 0 0 12px 12px;
    color: #fff; font-size: 44px; font-weight: 700;
    letter-spacing: 4px; text-align: center; line-height: 70px;
  }
  .tab-fold { position: absolute; top: 0; }

  .office-choice {
    position: absolute; top: 83px; left: 54px;
    display: flex; align-items: center;
    font-size: 24px; font-weight: 500; color: var(--text-gray);
  }
  .office-choice__box {
    width: 27px; height: 27px; border: 1px solid var(--rule);
    margin-right: 9px;
  }
  .office-choice__label { margin-right: 12px; }

  .field {
    position: absolute; border: 1px solid var(--rule);
    font-size: 24px; font-weight: 500; color: var(--text-gray);
    padding: 8px 13px;
  }
  .field--for { left: 54px; top: 120px; width: 705px; height: 150px; padding-top: 6px; }
  .field--date { left: 54px; top: 279px; width: 347px; height: 54px; line-height: 36px; }
  .field--time { left: 412px; top: 279px; width: 347px; height: 54px; line-height: 36px; }

  .notice {
    position: absolute; left: 0; right: 0; top: 344px;
    text-align: center; font-size: 24px; font-weight: 300;
    line-height: 32px; color: var(--brand-blue);
  }
  .notice strong { font-weight: 700; }

  .card-footer-stripe {
    position: absolute; left: 0; right: 0; bottom: 0; height: 17px;
    background: var(--brand-green);
  }
</style>
</head>
<body>

  <section class="card card--front">
    <div class="identity-mark"></div>
    <div class="practice-name">DANIEL R. WHITCOMBE MD PC</div>
    <div class="practice-tagline">ORTHOPAEDIC SURGERY &amp; SPORTS MEDICINE</div>

    <svg class="fold" style="left:50px" width="18" height="16"><polygon points="18,0 18,16 0,16" fill="#253a5a"/></svg>
    <svg class="fold" style="left:744px" width="18" height="16"><polygon points="0,0 18,16 0,16" fill="#253a5a"/></svg>
    <div class="credential-banner">Board Certified American Orthopedic Surgery</div>

    <div class="contact-band"></div>
    <div class="contact-band__base"></div>

    <div class="office office--bronx">
      <span class="office__rule"></span>
      <svg class="office__pointer" width="14" height="26"><polygon points="14,0 14,26 0,13" fill="#fff"/></svg>
      1487 Harrowgate Ave.<br>
      Suite KM7, Bronx NY 10527<br>
      Tel: (718) 552 - 1948<br>
      Fax: (718) 552 - 7210
    </div>

    <div class="office office--manhattan">
      <span class="office__rule"></span>
      <svg class="office__pointer" width="14" height="26"><polygon points="14,0 14,26 0,13" fill="#fff"/></svg>
      628 Fourth Ave.<br>
      Suite 42, New York,<br>
      NY 10087<br>
      Tel: (212) 734 - 2815
    </div>
  </section>

  <section class="card card--back">
    <svg class="tab-fold" style="left:197px" width="17" height="18"><polygon points="0,0 17,0 17,18" fill="#253a5a"/></svg>
    <svg class="tab-fold" style="left:595px" width="17" height="18"><polygon points="0,0 17,0 0,18" fill="#253a5a"/></svg>
    <div class="appointment-tab">APPOINTMENT</div>

    <div class="office-choice">
      <span class="office-choice__box"></span><span class="office-choice__label">Bronx</span>
      <span class="office-choice__box"></span><span class="office-choice__label">Mahattan</span>
    </div>

    <div class="field field--for">For:</div>
    <div class="field field--date">Date:</div>
    <div class="field field--time">Time:</div>

    <p class="notice">If you are unable to keep your appointment, Please call<br>
      <strong>(718) 263-5102</strong> 24hrs in advance.</p>

    <div class="card-footer-stripe"></div>
  </section>

</body>
</html>
```